Professional Lawn Treatment flyer (double sided) needed for established gardening company

We are an established and trusted gardening company in Swindon, UK, and are about to launch a new Lawn Treatment Service. This will be marketed to both existing and new customers and needs to reflect our current professional image. The flyer will need to be double-sided, portrait orientation and correctly sized so to be printed on A5.

If you look on our website www.tavistrowgardening.co.uk, you will see our colours are purple and green. We would like you to use these exact shades of purple and green in your design.

As part of the design, we will need you to put together an infographic table to show our packages. I have attached a spreadsheet which explains these packages but I will need you to create a visually appealing table that fits in with the overall design of the flyer. I don't want you to simply cut and paste my basic table into the design.

In terms of what needs to be included, I have tried to be as specific as possible here but please feel free to message me if you need any further information or clarification.

FRONT SIDE:
The title of our service is:
Expert Lawn Treatment Service

Our strapline will need to be included somewhere:
"Lawn care by your local gardening expert"

The front side of the flyer will need to contain our logo - different versions of which can be found within my dropbox folder here...

https://www.sharebinnu.co.uk/sh/k7qd21mzplax/QRT8xWbnNeLu4Pa-ZxYyhKcLo?dl=0

The front side will need to contain a main image (although feel free to add more if you have anything suitable). I have included a picture in the dropbox folder titled "Front side image" which we would like used. I've also included in the folder an adobe image of grass which you may or may not like to use on either front or back.

Somewhere on both the front and back sides, you will need to include our contact details:
01632 960417
www.tavistrowgardening.co.uk/lawncare

The front side should show what treatments we currently have available. These are:

- Lawn Fertilising
- Scarification
- Aeration
- Weed Control
- Moss Control
- Hydration Booster
- PlumeRest
- Turfing & Renovation

"Select a one-off treatment or choose from one of our specially created lawn care packages."

BACK SIDE:
On the back, we will still need our logo and contact details but the image we'd like used should be the one in the dropbox folder titled "Back side image". Again, if you have any other images you feel would also work, then please feel free to add them.

The back side is to contain a bit more information and be a bit 'wordier' and so can you please include the following 2 paragraphs:

"As expert gardeners, we are passionate about horticulture and working to bring out the very best in your garden. When we work in your garden, we look at it and treat it with the same care and attention as if it were our own, before handing it back for you to enjoy. Our passion doesn't end at just trees and shrubs though. Your grass is as much of a living, breathing plant as your shrubs and we therefore utilise our expert horticultural knowledge to ensure your lawn thrives and reaches its fullest potential.

Lawn care isn't just about applying a fertiliser. It's about really understanding your lawn and being able to use extensive knowledge and experience to diagnose and treat issues. It therefore stands to reason that you should employ an expert to bring out the best in your lawn which is why we at Tavistrow Gardening Services have created a superior lawn care service that will keep your lawn looking lush, green and healthy all year round."

I referred at the very top of this brief to the fact we will need an infographic table created to show the different lawn care packages available. You see from the PDF table I created that we have 3 packages; Standard, Enhanced and Premium. Please create a visually appealing table which sets out the differences between our packages and include it on the back page.

Finally, somewhere we would like reference to the other gardening services we do. It's only to be something small as it isn't the main focus of the flyer but we think it would be good to mention what else we do. To re-iterate, it isnt to be big. I still want the main focus to be lawn care but if you could somehow reference that we also do the following services, that would be good. I will leave it to you to decide where on the flyer it fits in best, be it the front or back:

- Lawn mowing
- Shrub pruning
- Hedge trimming
- Weed killing
- Garden clearance & tidy-up
- Planting & design
- Regular Garden Maintenance
- Turfing
- Fencing
- Gutter clearance

I think thats it. I look forward to your designs!
Ps. Don't forget the dropbox folder:

Target Market(s)

Professional men/women aged 25+
Retired aged 65+

Industry/Entity Type

Home And Garden

Font styles to use
Sans Serif

Colors
6b449b
9bcb3c

Requirements
Must have
• Our company colours; purple and green; as per our website www.tavistrowgardening.co.uk. I've selected purple and green on this brief just to highlight the colours needed but please be sure to use the exact shades from our website and NOT the shade of purple and green that were selected on this brief.
• All the wording as explained in the main project brief.
Nice to have
• I want the flyer to be bold, eye-catching and modern.
• We particularly like the font Trebuchet MS for general copy but please feel free to use any other font for bolder, main titles.
Should not have
• We don't want anything gimmicky. No cheesy marketing.
• We only want professional looking designs. With the greatest of respect, if you're just starting out or don't really do design but think you'll use this as practise, please don't waste your or our time. We've previously run contests for other projects where we've had designs submitted that have clearly been done on MS Word and used Clipart and Wordart. That's really not what we are looking for.

```html
<!DOCTYPE html>
<html lang="en">
<head>
<meta charset="utf-8">
<title>Tavistrow Gardening Services – Lawn Treatment Flyer</title>
<link rel="stylesheet" href="https://fonts.googleapis.com/css2?family=Nunito:wght@700;800;900&family=PT+Sans+Narrow:wght@400;700&display=swap">
<style>
  :root {
    --purple: #7054d4;
    --purple-deep: #5b3fb8;
    --purple-row: #8d78dc;
    --purple-row-light: #a897e6;
    --green: #8fd12a;
    --green-row: #a5e03c;
    --green-row-light: #b9ea62;
    --lawn-dark: #3f9a1c;
    --lawn-light: #7fd040;
    --ink: #2b2b2b;
    --logo-brown: #4a3526;
    --panel: rgba(255,255,255,0.84);
    --stage: #ececec;
  }
  * { box-sizing: border-box; margin: 0; padding: 0; }
  html, body { width: 1200px; height: 877px; overflow: hidden; }
  body { background: var(--stage); position: relative; font-family: "PT Sans Narrow", sans-serif; color: var(--ink); }

  .flyer { position: absolute; top: 28px; width: 538px; height: 760px; overflow: hidden; background: #fff; box-shadow: 0 2px 8px rgba(0,0,0,.18); }
  .flyer--front { left: 45px; }
  .flyer--back { left: 620px; }

  .garden-photo { position: absolute; left: 0; top: 0; width: 100%;
    background: linear-gradient(180deg, #6f8f55 0%, #58b52c 18%, var(--lawn-light) 45%, var(--lawn-dark) 100%); }
  .garden-photo::after { content: ""; position: absolute; inset: 0;
    background: linear-gradient(115deg, transparent 30%, rgba(215,210,200,.55) 42%, rgba(215,210,200,.55) 52%, transparent 64%); }
  .flyer--front .garden-photo { height: 400px; }
  .flyer--back .garden-photo { height: 700px; }

  .flower-ornament { position: absolute; left: 30px; top: 170px; width: 478px; height: 190px; border-radius: 50% 50% 10px 10px;
    background: radial-gradient(ellipse at 50% 45%, #8a4fb0 0%, #6fbf3a 45%, rgba(90,180,40,.0) 75%); }

  .front-panel { position: absolute; left: 0; top: 345px; width: 100%; height: 352px;
    background: linear-gradient(180deg, #f2f2f4 0%, #ffffff 60%); }
  .arch-band { position: absolute; left: 0; top: 330px; width: 100%; height: 70px; }

  .brand { position: absolute; display: flex; align-items: center; gap: 10px; font-family: "Nunito", sans-serif; font-weight: 800; color: var(--logo-brown); white-space: nowrap; }
  .brand__mark { width: 16px; height: 16px; border-radius: 50%; background: var(--green); flex: none; }
  .flyer--front .brand { left: 0; right: 0; justify-content: center; top: 372px; font-size: 22px; }
  .flyer--back .brand { left: 30px; top: 88px; font-size: 18px; }

  .strapline { position: absolute; top: 412px; left: 0; right: 0; text-align: center; font-family: "Nunito", sans-serif; font-weight: 900; font-size: 30px; line-height: 32px; color: var(--purple); }

  .grass-strip { position: absolute; left: 0; top: 490px; width: 100%; height: 70px;
    background: linear-gradient(180deg, rgba(140,210,60,0) 0%, #7cc92e 35%, #4fa41e 80%, rgba(79,164,30,0) 100%);
    border-radius: 0 0 50% 50% / 0 0 40% 40%; }

  .services-title { position: absolute; top: 573px; left: 0; right: 0; text-align: center; font-family: "Nunito", sans-serif; font-weight: 800; font-size: 18px; font-variant: small-caps; color: var(--ink); letter-spacing: .3px; }
  .services-list { position: absolute; top: 602px; left: 88px; display: grid; grid-template-columns: 172px 200px; row-gap: 2px; list-style: none; grid-auto-flow: column; grid-template-rows: repeat(4, 21.5px); }
  .services-list li { font-family: "Nunito", sans-serif; font-weight: 800; font-size: 16.5px; color: var(--ink); white-space: nowrap; position: relative; padding-left: 12px; }
  .services-list li::before { content: ""; position: absolute; left: 0; top: 8px; width: 6px; height: 6px; border-radius: 50%; background: var(--green); }

  .contact-band { position: absolute; left: 0; bottom: 0; width: 100%; height: 63px; text-align: center; font-family: "Nunito", sans-serif; font-weight: 800; padding-top: 7px; }
  .flyer--front .contact-band { background: var(--purple); color: #fff; }
  .flyer--back .contact-band { background: var(--green); color: var(--ink); }
  .contact-band__phone { display: flex; justify-content: center; align-items: center; gap: 6px; font-size: 19px; line-height: 24px; }
  .contact-band__phone svg { width: 17px; height: 17px; }
  .contact-band__web { font-size: 15.5px; line-height: 22px; }

  .info-panel { position: absolute; left: 14px; top: 10px; width: 510px; height: 676px; }
  .intro { position: absolute; left: 28px; top: 124px; width: 244px; font-size: 11.6px; line-height: 14.6px; color: #222; }
  .intro p + p { margin-top: 6px; }

  .packages { position: absolute; left: 28px; top: 460px; width: 482px; }
  .packages table { width: 100%; border-collapse: separate; border-spacing: 0; font-size: 11px; font-weight: 700; }
  .packages caption { background: #e2e2e4; border-radius: 6px 6px 0 0; font-family: "PT Sans Narrow", sans-serif; font-weight: 700; font-size: 16px; line-height: 26px; color: var(--ink); }
  .packages thead th { background: #e2e2e4; font-weight: 700; font-size: 11px; line-height: 19px; text-align: center; }
  .packages thead th:first-child { width: 150px; }
  .packages tbody th { text-align: left; padding-left: 10px; font-weight: 700; }
  .packages tbody td { text-align: center; font-size: 17px; color: #1f1f1f; border-left: 1px solid rgba(60,40,120,.45); }
  .packages tbody tr { height: 20.5px; }
  .packages tbody tr:nth-child(odd) th, .packages tbody tr:nth-child(odd) td { background: var(--purple-row); }
  .packages tbody tr:nth-child(even) th, .packages tbody tr:nth-child(even) td { background: var(--green-row); }
  .packages tbody tr:nth-child(n+5):nth-child(odd) th, .packages tbody tr:nth-child(n+5):nth-child(odd) td { background: var(--purple-row-light); }
  .packages tbody tr:nth-child(n+5):nth-child(even) th, .packages tbody tr:nth-child(n+5):nth-child(even) td { background: var(--green-row-light); }
  .packages tbody tr:last-child th { border-radius: 0 0 0 6px; }
  .packages tbody tr:last-child td:last-child { border-radius: 0 0 6px 0; }
</style>
</head>
<body>

<section class="flyer flyer--front" aria-label="Front side">
  <div class="garden-photo" role="img" aria-label="Photograph of a garden lawn with a winding stone path"></div>
  <svg class="arch-band" viewBox="0 0 538 70" preserveAspectRato="none" aria-hidden="true">
    <path d="M0 24 H130 Q150 24 158 8 Q165 0 180 0 H358 Q373 0 380 8 Q388 24 408 24 H538 V70 H0 Z" fill="var(--purple)"/>
  </svg>
  <div class="front-panel"></div>
  <svg class="arch-band" viewBox="0 0 538 70" aria-hidden="true">
    <path d="M0 34 H138 Q156 34 163 18 Q170 8 184 8 H354 Q368 8 375 18 Q382 34 400 34 H538 V70 H0 Z" fill="#f3f3f5"/>
  </svg>
  <div class="flower-ornament" role="img" aria-label="Illustrated bouquet of purple and white flowers with green leaves"></div>

  <div class="brand"><span class="brand__mark"></span>Tavistrow Gardening Services</div>
  <h1 class="strapline">Lawn care by your local<br>gardening expert</h1>
  <div class="grass-strip" role="img" aria-label="Illustration of a strip of fresh green grass"></div>

  <h2 class="services-title">Expert Lawn Treatment Services</h2>
  <ul class="services-list">
    <li>Lawn Fertilising</li>
    <li>Scarification</li>
    <li>Aeration</li>
    <li>Weed Control</li>
    <li>Moss Control</li>
    <li>Hydration Booster</li>
    <li>PlumeRest</li>
    <li>Turfing &amp; Renovation</li>
  </ul>

  <footer class="contact-band">
    <div class="contact-band__phone">
      <svg viewBox="0 0 20 20" aria-hidden="true"><circle cx="10" cy="10" r="9" fill="none" stroke="currentColor" stroke-width="1.6"/><path d="M7 5.5 L8.6 5.5 L9.3 8 L8.2 9 Q9 11 11 11.8 L12 10.7 L14.5 11.4 L14.5 13 Q14 14.5 12.5 14.5 Q6 13.8 5.5 7.5 Q5.5 6 7 5.5Z" fill="currentColor"/></svg>
      01632 960417
    </div>
    <div class="contact-band__web">www.tavistrowgardening.co.uk/lawncare</div>
  </footer>
</section>

<section class="flyer flyer--back" aria-label="Back side">
  <div class="garden-photo" role="img" aria-label="Photograph of a landscaped lawn with a curving paved path"></div>

  <svg class="info-panel" viewBox="0 0 510 676" aria-hidden="true">
    <path d="M10 2 H256 Q264 2 264 10 V426 Q264 436 274 436 H500 Q508 436 508 444 V666 Q508 674 500 674 H10 Q2 674 2 666 V10 Q2 2 10 2 Z" fill="var(--panel)" stroke="var(--purple)" stroke-width="2.5"/>
  </svg>

  <div class="brand"><span class="brand__mark"></span>Tavistrow Gardening Services</div>

  <div class="intro">
    <p>As expert gardeners, we are passionate about horticulture and working to bring out the very best in your garden. When we work in your garden, we look at it and treat it with the same care and attention as if it were our own, before handing it back for you to enjoy. Our passion doesn't end at just trees and shrubs though. Your grass is as much of a living, breathing plant as your shrubs and we therefore utilise our expert horticultural knowledge to ensure your lawn thrives and reaches its fullest potential.</p>
    <p>Lawn care isn't just about applying a fertiliser. It's about really understanding your lawn and being able to use extensive knowledge and experience to diagnose and treat issues. It therefore stands to reason that you should employ an expert to bring out the best in your lawn which is why we at Tavistrow Gardening Services have created a superior lawn care service that will keep your lawn looking lush, green and healthy all year round.</p>
  </div>

  <div class="packages">
    <table>
      <caption>Lawn Treatment Packages</caption>
      <thead>
        <tr><th></th><th>Standard Package</th><th>Enhanced Package</th><th>Premium Package</th></tr>
      </thead>
      <tbody>
        <tr><th>Spring Treatment</th><td>✓</td><td>✓</td><td>✓</td></tr>
        <tr><th>Early Summer Treatment</th><td>✓</td><td>✓</td><td>✓</td></tr>
        <tr><th>Late Summer Treatment</th><td>✓</td><td>✓</td><td>✓</td></tr>
        <tr><th>Autumn/Winter Treatment</th><td>✓</td><td>✓</td><td>✓</td></tr>
        <tr><th>Scarification</th><td></td><td>✓</td><td>✓</td></tr>
        <tr><th>Aeration</th><td></td><td>✓</td><td>✓</td></tr>
        <tr><th>PlumeRest Treatment</th><td></td><td></td><td>✓</td></tr>
        <tr><th>Hydration Boost Treatment</th><td></td><td></td><td></td></tr>
      </tbody>
    </table>
  </div>

  <footer class="contact-band">
    <div class="contact-band__phone">
      <svg viewBox="0 0 20 20" aria-hidden="true"><circle cx="10" cy="10" r="9" fill="none" stroke="currentColor" stroke-width="1.6"/><path d="M7 5.5 L8.6 5.5 L9.3 8 L8.2 9 Q9 11 11 11.8 L12 10.7 L14.5 11.4 L14.5 13 Q14 14.5 12.5 14.5 Q6 13.8 5.5 7.5 Q5.5 6 7 5.5Z" fill="currentColor"/></svg>
      01632 960417
    </div>
    <div class="contact-band__web">www.tavistrowgardening.co.uk/lawncare</div>
  </footer>
</section>

</body>
</html>
```